Folderdesign für Hundeshop und Hundesalon Pfote Mirella
Zielgruppe
Hundesalon ( pfote-mirella.de)
Hundeshop mit Onlineshop (hundeshop-pfote-mirella.de)
Zielgruppe: Hundebesitzer
Aufgabenstellung
Das Design sollte klar strukturiert und keinesfalls überladen sein, sondern mit einem Blick gut zu erfassen sein, farblich passend zu Naturkauartikeln, Kauartikeln ohne chem. Zusatzstoffe,...s Homepage
Erste Seite soll Hundesalon UND Hundeshop bewerben
Hervorgehoben werden soll der Hundeshop, da er als Onlineshop neu ist. Die Informationen entnehmen Sie bitte der HP www.hundeshop-pfote-mirella.de.
Der Hundesalon soll eine Seite bekommen
DIN A 4 Wickelfalz, 6seitig...lasse mich aber gerne beraten falls jemand etwas anderes besser findet
Habe schon mal einen Flyer entworfen, aber er sieht mir zu normal und einfach aus. Texte können auch gerne verändert werden

```html
<!DOCTYPE html>
<html lang="de">
<head>
<meta charset="utf-8">
<title>Pfote Mirella – Folder</title>
<link href="https://fonts.googleapis.com/css2?family=Great+Vibes&family=Ubuntu:wght@400;500&display=swap" rel="stylesheet">
<style>
  :root {
    --green: #7cb342;
    --green-light: #9ccc5a;
    --green-dark: #5f9a2e;
    --paper: #ffffff;
    --paper-grey: #eceeed;
    --stage: #e4e6e5;
    --ink: #2b2b2b;
    --photo-light: #dcdcdc;
    --photo-mid: #b8a58a;
  }
  * { box-sizing: border-box; margin: 0; padding: 0; }
  html, body { width: 1200px; height: 800px; overflow: hidden; }
  body {
    background: var(--stage);
    font-family: "Ubuntu", sans-serif;
    display: flex; align-items: center; justify-content: center; gap: 36px;
  }
  .panel {
    position: relative; width: 350px; height: 740px;
    background: var(--paper); overflow: hidden;
    box-shadow: 0 6px 18px rgba(0,0,0,.18);
  }
  .panel svg.shapes { position: absolute; inset: 0; }
  .script { font-family: "Great Vibes", cursive; font-weight: 400; }

  /* cover */
  .cover { background: linear-gradient(180deg, var(--paper) 0%, var(--paper-grey) 60%, var(--paper) 100%); }
  .cover .brand {
    position: absolute; left: 40px; top: 62px; width: 210px; text-align: center;
    font-size: 36px; font-weight: 500; color: var(--ink); line-height: 1.05;
    letter-spacing: 1px;
  }
  .cover .jump-photo {
    position: absolute; left: 258px; top: 40px; width: 62px; height: 118px;
    border-radius: 30px; background: linear-gradient(180deg, #f2f2f2, #cfcfcf);
  }
  .cover .dogs-photo {
    position: absolute; left: 0; top: 250px; width: 350px; height: 320px;
    background: linear-gradient(160deg, var(--photo-light) 0%, #efefef 45%, var(--photo-mid) 100%);
  }
  .cover .claim {
    position: absolute; left: 0; right: 0; bottom: 56px; text-align: center;
    color: #fff; font-size: 44px;
  }

  /* salon panel */
  .salon .title { position: absolute; left: 40px; top: 40px; color: var(--green); font-size: 46px; }
  .salon .tagline {
    position: absolute; left: 48px; top: 102px; color: var(--green);
    font-size: 17px; font-weight: 500; line-height: 1.25;
  }
  .salon .greeting { position: absolute; left: 28px; top: 168px; color: var(--green); font-size: 22px; }
  .salon .body {
    position: absolute; left: 28px; right: 28px; top: 204px; color: var(--green);
    font-size: 13.5px; line-height: 1.5; text-align: justify;
  }
  .salon .body p + p { margin-top: 8px; }
  .salon .portrait {
    position: absolute; left: -20px; top: 392px; width: 150px; height: 150px; border-radius: 50%;
    border: 4px solid #f4f4f4; box-shadow: 0 2px 6px rgba(0,0,0,.2);
    background: radial-gradient(circle at 55% 55%, #f7f3ec 0%, #e3d8c6 60%, #b99e7a 100%);
  }
  .salon .signature {
    position: absolute; left: 180px; top: 420px; color: var(--green); font-size: 26px; line-height: 1.15;
  }
  .salon .mark {
    position: absolute; left: 170px; top: 500px; width: 160px; color: var(--ink); text-align: center;
  }
  .salon .mark small { display: block; font-size: 11px; line-height: 1.3; }
  .salon .mark strong { display: block; font-size: 17px; font-weight: 500; margin-top: 4px; letter-spacing: 1px; }
  .salon .contact {
    position: absolute; left: 28px; top: 582px; color: #fff; font-size: 13px; font-weight: 500;
    line-height: 1.4; font-style: normal;
  }
  .salon .contact .gap { margin-top: 6px; }
</style>
</head>
<body>

<section class="panel cover" aria-label="Titelseite">
  <svg class="shapes" width="350" height="740" viewBox="0 0 350 740" aria-hidden="true">
    <path d="M0 0 H350 V150 C280 210 120 235 0 200 Z" fill="var(--green)"/>
    <ellipse cx="178" cy="110" rx="170" ry="95" fill="var(--paper)"/>
    <path d="M10 170 C90 235 250 235 350 160 L350 175 C250 245 90 245 10 175 Z" fill="var(--green-light)"/>
    <path d="M0 585 C120 570 240 575 350 600 V740 H0 Z" fill="var(--green)"/>
    <path d="M0 585 C120 570 240 575 350 600 V612 C240 588 120 582 0 597 Z" fill="var(--green-light)"/>
  </svg>
  <div class="brand">Pfote<br>Mirella</div>
  <div class="jump-photo" role="img" aria-label="Foto: springender kleiner Terrier"></div>
  <div class="dogs-photo" role="img" aria-label="Foto: Schäferhund, Golden Retriever und Dalmatiner vor hellem Hintergrund"></div>
  <h1 class="claim script">Hundesalon + Shop</h1>
</section>

<section class="panel salon" aria-label="Hundesalon">
  <svg class="shapes" width="350" height="740" viewBox="0 0 350 740" aria-hidden="true">
    <path d="M0 0 H40 C30 60 20 120 0 160 Z" fill="var(--green)"/>
    <circle cx="330" cy="90" r="80" fill="var(--green)"/>
    <circle cx="360" cy="90" r="32" fill="var(--paper)"/>
    <path d="M0 550 C120 585 250 612 350 600 V740 H0 Z" fill="var(--green)"/>
    <path d="M0 550 C120 585 250 612 350 600 V611 C250 623 120 596 0 561 Z" fill="var(--green-light)"/>
  </svg>
  <h2 class="title script">Hundesalon</h2>
  <p class="tagline">… weil Fellpflege<br>Vertrauen braucht!</p>
  <p class="greeting script">Liebe Kunden,</p>
  <div class="body">
    <p>der Hund ist unser treuester Begleiter – er hat es verdient, optimal versorgt zu werden.</p>
    <p>Gesunde Ernährung und gute Pflege können viel dazu beitragen.</p>
    <p>Pfote Mirella bietet beides an: einen Hundeshop mit hochwertigen Artikeln und einen Hundesalon mit liebevoller Einzelbetreuung.</p>
  </div>
  <div class="portrait" role="img" aria-label="Foto: weißer Malteser im Rundbild"></div>
  <p class="signature script">Ihre Jana<br>&nbsp;&nbsp;Wolters</p>
  <div class="mark">
    <small>Hundesalon<br>&amp;<br>Hundeshop</small>
    <strong>PFOTE MIRELLA</strong>
  </div>
  <address class="contact">
    Jana Wolters<br>
    Am Lindenhang 19<br>
    45100 Birkental
    <div class="gap">Tel. 0201 / 55 12 34 56<br>Mobil 0170 / 98 76 543</div>
    <div class="gap">info@pfote-mirella.de<br>www.pfote-mirella.de</div>
  </address>
</section>

</body>
</html>
```